Home Security Company Business Card

Looking for a eye catching business card that is non traditional and stands out but yet still looks professional. It should include all the pertinent information such as name, title, address, telephone, e-mail, website address should definitely stand out and then finally the logo.

Target Market(s)

Residential and Commercial accounts mostly upscale accounts

Industry/Entity Type

Security

Contact Information for Business Card

Name
Title
Address
Office #
Cell #
E-mail
Website

Font styles to use
Serif
Sans Serif

Requirements
Must have
• Logo, two sided color configuration
Nice to have
• You decide
Should not have
• There really aren't any.

```html
<!DOCTYPE html>
<html lang="en">
<head>
<meta charset="utf-8">
<title>Keystone Guard Services Inc. – Business Card</title>
<link href="https://fonts.googleapis.com/css2?family=Open+Sans:wght@400;700&family=Libre+Baskerville&display=swap" rel="stylesheet">
<style>
  :root {
    --bg: #e9e4df;
    --wine-light: #a83242;
    --wine: #8a1c28;
    --wine-dark: #5e0c14;
    --gold: #e7b648;
    --gold-deep: #c98f23;
    --white: #ffffff;
    --cream: #f3e6e6;
  }
  * { margin: 0; padding: 0; box-sizing: border-box; }
  html, body { width: 1200px; height: 913px; overflow: hidden; }
  body {
    background: var(--bg);
    font-family: "Open Sans", Arial, sans-serif;
    position: relative;
  }
  .card {
    position: absolute;
    top: 308px;
    width: 520px;
    height: 297px;
    border-radius: 4px;
    overflow: hidden;
    background: linear-gradient(160deg, var(--wine-light) 0%, var(--wine) 45%, var(--wine-dark) 100%);
    box-shadow: 0 10px 24px rgba(0,0,0,.25);
    color: var(--white);
  }
  .card--front { left: 50px; }
  .card--back { left: 630px; }
  .card__shapes { position: absolute; inset: 0; }
  .brand {
    position: absolute;
    display: flex;
    align-items: center;
    gap: 10px;
    font-family: "Libre Baskerville", "Times New Roman", serif;
    color: var(--white);
    text-transform: uppercase;
    line-height: 1;
  }
  .brand__dot {
    width: 26px; height: 26px;
    border-radius: 50%;
    background: var(--gold);
    flex: none;
  }
  .brand__name { font-size: 15px; letter-spacing: .5px; }
  .card--front .brand { top: 44px; left: 250px; }
  .card--back .brand { top: 110px; left: 110px; }
  .card--back .brand__dot { width: 40px; height: 40px; }
  .card--back .brand__name { font-size: 20px; }
  .person { position: absolute; left: 32px; top: 132px; }
  .person__name { font-weight: 700; font-size: 23px; }
  .person__title { color: var(--gold); font-size: 13px; text-align: right; margin-top: -2px; }
  .person__address { font-size: 14px; line-height: 1.45; margin-top: 4px; color: var(--cream); }
  .contacts {
    position: absolute; left: 282px; top: 108px;
    list-style: none; font-size: 13px; line-height: 1.55;
  }
  .contacts li { display: flex; align-items: center; gap: 8px; }
  .contacts svg { width: 11px; height: 11px; fill: var(--gold); flex: none; }
  .website {
    position: absolute; left: 0; right: 0; top: 200px;
    text-align: center; color: var(--gold); font-size: 15px; letter-spacing: .3px;
  }
</style>
</head>
<body>

<section class="card card--front">
  <svg class="card__shapes" viewBox="0 0 520 297" aria-hidden="true">
    <line x1="0" y1="128" x2="245" y2="128" stroke="var(--cream)" stroke-width="1"/>
    <polygon points="345,240 520,166 520,196 360,268" fill="var(--gold)"/>
    <polygon points="0,274 320,238 334,262 0,297" fill="var(--white)"/>
  </svg>
  <div class="brand"><span class="brand__dot"></span><span class="brand__name">Keystone Guard<br>Services Inc.</span></div>
  <div class="person">
    <div class="person__name">Daniel Whitmore</div>
    <div class="person__title">Owner</div>
    <div class="person__address">248 Harbor Lane<br>Maple Falls, Ohio 44012</div>
  </div>
  <ul class="contacts">
    <li><svg viewBox="0 0 24 24"><path d="M3 9c0-3 4-5 9-5s9 2 9 5v2h-5V9c-1-1-7-1-8 0v2H3zM6 12h12l2 8H4z"/></svg>+555 2460-0198</li>
    <li><svg viewBox="0 0 24 24"><path d="M6 2l4 5-2 3c1 3 3 5 6 6l3-2 5 4-3 4C10 22 2 14 2 5z"/></svg>+5550140-22871</li>
    <li><svg viewBox="0 0 24 24"><path d="M2 5h20v14H2zM4 7l8 6 8-6v-.5H4z" fill-rule="evenodd"/></svg>info@danielwhitmoremail.com</li>
  </ul>
</section>

<section class="card card--back">
  <div class="brand"><span class="brand__dot"></span><span class="brand__name">Keystone Guard<br>Services Inc.</span></div>
  <div class="website">www.keystoneguardservicesinc.com</div>
</section>

</body>
</html>
```